Business Card Design

Business Card for professional consulting firm working with large financial institutions.

Target Market(s)

Executive buyers

Industry/Entity Type

Banking

Contact Information for Business Card

Mild creativity wanted. Not boring, but do elaborate artwork.

Font styles to use
Serif
Sans Serif

Colors

Designer to choose colors to be used in the design.

Requirements
Must have
• Standard business card features - company name, individual name, telephone, website, email, locations.
Nice to have
• Two colors
Should not have
• too many colors, fancy printing, cartoons.

```html
<!DOCTYPE html>
<html lang="en">
<head>
<meta charset="utf-8">
<title>Veranth Partners — Business Card</title>
<link rel="stylesheet" href="https://fonts.googleapis.com/css2?family=Merriweather:wght@400;700;900&family=Source+Sans+3:wght@400;600&display=swap">
<style>
  :root {
    --stage: #2a2c30;
    --card-white: #ffffff;
    --card-black: #0c0c0d;
    --ink: #1b1b1b;
    --ink-soft: #4a4a4a;
    --silver: #a9a9ab;
    --silver-dark: #6f6f72;
  }
  * { box-sizing: border-box; margin: 0; padding: 0; }
  html, body {
    width: 1200px; height: 900px; overflow: hidden;
    background: var(--stage);
  }
  .stage {
    width: 1200px; height: 900px;
    display: flex; flex-direction: column;
    align-items: center; justify-content: center; gap: 48px;
  }
  .card {
    position: relative;
    width: 630px; height: 360px;
    border-radius: 22px;
    overflow: hidden;
    box-shadow: 0 18px 40px rgba(0,0,0,.45);
  }

  /* Front */
  .card-front { background: var(--card-white); color: var(--ink); }
  .person { position: absolute; left: 46px; top: 44px; }
  .person-name {
    font-family: "Merriweather", serif; font-weight: 900;
    font-size: 21px; letter-spacing: .3px;
  }
  .person-title {
    font-family: "Source Sans 3", sans-serif; font-size: 11px;
    letter-spacing: 1px; color: var(--ink-soft); margin-top: 2px;
  }
  .person-rule { width: 38px; height: 2px; background: var(--ink); margin-top: 14px; }
  .contact-list { list-style: none; position: absolute; left: 46px; top: 128px; }
  .contact-item {
    display: flex; align-items: center; gap: 14px;
    font-family: "Merriweather", serif; font-size: 14px; color: var(--ink);
    height: 31px;
  }
  .contact-icon { width: 16px; height: 16px; fill: var(--ink); flex: none; }

  .brand {
    position: absolute;
    font-family: "Merriweather", serif; font-weight: 400;
    letter-spacing: .5px;
  }
  .card-front .brand { left: 312px; top: 128px; font-size: 30px; color: var(--ink); }

  .address {
    position: absolute; right: 40px; bottom: 36px; text-align: right;
    font-family: "Merriweather", serif; font-size: 15px; line-height: 1.55; color: var(--ink);
  }
  .corner-band {
    position: absolute; left: 0; bottom: 0; width: 100%; height: 100%;
  }

  /* Back */
  .card-back {
    background: linear-gradient(160deg, #1a1a1b 0%, var(--card-black) 55%, #050505 100%);
  }
  .card-back .brand {
    left: 0; right: 0; top: 50%; transform: translateY(-50%);
    text-align: center; font-size: 40px; color: var(--silver);
  }
</style>
</head>
<body>
<main class="stage">

  <section class="card card-front" aria-label="Business card front">
    <svg class="corner-band" viewBox="0 0 630 360" aria-hidden="true">
      <path d="M0 250 L150 250 L210 360 L0 360 Z" fill="var(--silver)"/>
      <path d="M0 262 L142 262 L196 360 L0 360 Z" fill="var(--card-black)"/>
    </svg>

    <div class="person">
      <h1 class="person-name">JOHNATHAN DOE</h1>
      <p class="person-title">DIRECTOR</p>
      <div class="person-rule"></div>
    </div>

    <ul class="contact-list">
      <li class="contact-item">
        <svg class="contact-icon" viewBox="0 0 16 16" aria-hidden="true"><path d="M3.5 1.5l2.5 0 1 3-1.6 1.2a8 8 0 0 0 4.9 4.9L11.5 9l3 1v2.5c0 1-1 2-2 2C6.5 14.5 1.5 9.5 1.5 3.5c0-1 1-2 2-2z"/></svg>
        <span>123 456 789</span>
      </li>
      <li class="contact-item">
        <svg class="contact-icon" viewBox="0 0 16 16" aria-hidden="true"><path d="M1 3h14v10H1z M1.5 3.5L8 9l6.5-5.5" fill="var(--ink)"/><path d="M1.8 4L8 8.8 14.2 4" stroke="#fff" stroke-width="1.2" fill="none"/></svg>
        <span>email@domainname.com</span>
      </li>
      <li class="contact-item">
        <svg class="contact-icon" viewBox="0 0 16 16" aria-hidden="true"><circle cx="8" cy="8" r="7"/><path d="M1 8h14M8 1v14M3 4.2h10M3 11.8h10M8 1c-3 3-3 11 0 14M8 1c3 3 3 11 0 14" stroke="#fff" stroke-width=".9" fill="none"/></svg>
        <span>www.websiteaddress.com</span>
      </li>
    </ul>

    <p class="brand">Veranth Partners</p>

    <address class="address">Address Line 1<br>Second Line, Zip Code 1243</address>
  </section>

  <section class="card card-back" aria-label="Business card back">
    <p class="brand">Veranth Partners</p>
  </section>

</main>
</body>
</html>
```